Vorna Fleet business card

I am needing a business card that at a glance shows all the services that we provide emphasizing some more than others. We are a Fleet and Compliance management company as well as a software company. We provide outsourced solutions for KPX compliance and HR services via our own software.
In addition, we do
drug testing
GPS
Cameras
Electronic DVIRS
ELD's

Target Market(s)

Transportation company owners

Industry/Entity Type

Transportation supplier

Contact Information for Business Card

the card should inform potential customers what we do

Other font styles liked:
• I have added brand guidelines. See attached

Requirements
Must have
• See description
Should not have
• Colors outside my brand guide. See attached

```html
<!DOCTYPE html>
<html lang="en">
<head>
<meta charset="UTF-8">
<title>Vorna Fleet – Business Card</title>
<link href="https://fonts.googleapis.com/css2?family=Arimo:wght@400;700&display=swap" rel="stylesheet">
<style>
  :root {
    --backdrop: #e4e4e2;
    --card: #2a2a2d;
    --card-deep: #1b1b1d;
    --red: #e51f2a;
    --edge: #b5141d;
    --white: #f2f2f2;
    --muted: #d6d6d6;
    --ghost: #4a4a4d;
    --band-line: #3a3a3d;
  }
  * { box-sizing: border-box; margin: 0; padding: 0; }
  html, body { width: 1200px; height: 801px; overflow: hidden; }
  body {
    background: var(--backdrop);
    font-family: "Arimo", Arial, sans-serif;
    position: relative;
  }
  .card {
    position: absolute;
    top: 246px;
    width: 540px;
    height: 309px;
    background: var(--card);
    border-bottom: 4px solid var(--edge);
    overflow: hidden;
  }
  .card--front { left: 40px; }
  .card--back {
    left: 620px;
    background: linear-gradient(160deg, var(--card) 0%, var(--card-deep) 100%);
  }

  /* Front */
  .brand {
    position: absolute;
    top: 48px; left: 0; right: 0;
    display: flex; align-items: center; justify-content: center; gap: 12px;
  }
  .brand__square { width: 22px; height: 22px; background: var(--red); }
  .brand__name {
    font-weight: 700; font-size: 40px; line-height: 1;
    color: var(--white); letter-spacing: 0.5px;
  }
  .details {
    position: absolute;
    top: 140px; left: 0; right: 0;
    display: flex; justify-content: center; align-items: center; gap: 22px;
  }
  .person { text-align: right; }
  .person__name { color: var(--red); font-weight: 700; font-size: 22px; }
  .person__role { color: var(--white); font-size: 15px; margin-top: 3px; }
  .divider { width: 1px; height: 80px; background: var(--muted); opacity: 0.7; }
  .contacts { list-style: none; }
  .contacts li {
    display: flex; align-items: center; gap: 8px;
    color: var(--white); font-size: 14px; line-height: 24px;
  }
  .contacts svg { width: 12px; height: 12px; fill: var(--red); flex: none; }
  .address {
    position: absolute; left: 0; right: 0; top: 250px;
    text-align: center; color: var(--white); font-size: 14px;
  }

  /* Back */
  .watermark {
    position: absolute; top: 52px; left: 0; right: 0;
    text-align: center; white-space: nowrap;
    font-weight: 700; font-size: 76px; line-height: 1;
    color: var(--ghost); letter-spacing: -1px;
  }
  .services__title {
    position: absolute; top: 176px; left: 0; right: 0;
    text-align: center; color: var(--red);
    font-weight: 700; font-size: 24px; line-height: 1;
  }
  .services__band {
    position: absolute; left: 0; right: 0; top: 225px; bottom: 0;
    background: var(--card);
    border-top: 1px solid var(--band-line);
  }
  .services__list {
    position: absolute; top: 250px; left: 0; right: 0;
    list-style: none; display: flex; justify-content: center; flex-wrap: nowrap;
    padding: 0 16px;
  }
  .services__list li {
    color: var(--muted); font-weight: 700; font-size: 13.5px;
    text-transform: uppercase; white-space: nowrap;
  }
  .services__list li::before {
    content: "•"; color: var(--red); margin: 0 6px; font-size: 16px;
  }
</style>
</head>
<body>
  <section class="card card--front" aria-label="Card front">
    <div class="brand">
      <span class="brand__square"></span>
      <span class="brand__name">Vorna Fleet</span>
    </div>
    <div class="details">
      <div class="person">
        <p class="person__name">Elias Marlow</p>
        <p class="person__role">Manager</p>
      </div>
      <span class="divider"></span>
      <ul class="contacts">
        <li><svg viewBox="0 0 24 24"><path d="M6.6 10.8a15 15 0 0 0 6.6 6.6l2.2-2.2a1 1 0 0 1 1-.25 11.4 11.4 0 0 0 3.6.6 1 1 0 0 1 1 1V20a1 1 0 0 1-1 1A17 17 0 0 1 3 4a1 1 0 0 1 1-1h3.5a1 1 0 0 1 1 1c0 1.25.2 2.45.6 3.6a1 1 0 0 1-.25 1z"/></svg>123-456-2100</li>
        <li><svg viewBox="0 0 24 24"><path d="M2 5h20v2l-10 7L2 7z M2 9.5l10 7 10-7V19H2z"/></svg>youremail@mailbox.com</li>
        <li><svg viewBox="0 0 24 24"><circle cx="12" cy="12" r="10"/></svg>www.yourwebsite.com</li>
      </ul>
    </div>
    <p class="address">Your address, city, state, ZIP 0000</p>
  </section>

  <section class="card card--back" aria-label="Card back">
    <p class="watermark" aria-hidden="true">Vorna Fleet</p>
    <div class="services__band"></div>
    <h2 class="services__title">OUR SERVICES</h2>
    <ul class="services__list">
      <li>Drug Testing</li>
      <li>GPS</li>
      <li>Cameras</li>
      <li>Electronic DVIRS</li>
      <li>ELD's</li>
    </ul>
  </section>
</body>
</html>
```